MES Modul-Struktur grafisch veranschaulichen
Zielgruppe
Wir sind Software-Hersteller. Thema 'MES'. Unsere Kunden sind Produktionsunternehmen.
Mit einem MES (Manufacturing Execution System) werden Produktionsprozesse überwacht, geplant, gesteuert und optimiert. Allgemein geht es darum, die Produktivität zu steigern und Kosten zu minimieren.
Eine MES-Software ist modular strukturiert, so dass der Kunde sich nach Bedarf die einzelnen Funktionsmodule zusammenstellen kann. Unser MES MORVIK 7 MAX besteht z.B. aus folgenden Einzelmodulen:
- BASIS (Basismodul)
- MDE (Maschinendatenerfassung)
- BDE (Betriebsdatenerfassung)
- INST (Instandhaltung)
- ALARM (Alarmierung)
- DOK (Dokumentenmanagement)
- TNT (Traceability)
- PLAN (Feinplanung/Leitstand)
- LOG (Logistik)
- VIS (Visualisierung)
- PEP (Personaleinsatzplanung)
- MPZE (Personalzeiterfassung)
- DNC (Rezepturen/DNC)
- EM (Energiemonitoring)
Aufgabenstellung
Die modulare Struktur und der große Umfang an Modulen ist ein wichtiger Vorteil für unsere Kunden, da Sie nicht so schnell an Grenzen stoßen und sich dann unter Umständen eine weitere Insellösung (extra Software mit extra Datenbank ...) anschaffen müssen.
Wichtig ist, dass die einzelnen Module funktionell ineinandergreifen und alle auf die gleiche Datenbank zugreifen.
Es reicht wenn in der Grafik die Module nur mit er Abkürzung, also z.B. MDE bezeichnet werden. Für den ersten Entwurf können auch Platzhalter genutzt werden.
Der Betrachter sollte aus der Grafik auf den ersten Blick erkennen:
- umfängliches MES
- modular strukturiert
- Funktionsmodule step-by-step erweiterbar
Für die Umsetzung naheliegend wären Puzzle-Steine, Stapolos, ... muss aber nicht.

```html
<!DOCTYPE html>
<html lang="de">
<head>
<meta charset="utf-8">
<title>MES Modulstruktur – MORVIK 7 MAX</title>
<link rel="stylesheet" href="https://fonts.googleapis.com/css2?family=Open+Sans:wght@600;700&display=swap">
<style>
  :root{
    --bg-center:#ffffff;
    --bg-edge:#d3d8dc;
    --frame:#ffffff;
    --label:#ffffff;
  }
  html,body{margin:0;padding:0;overflow:hidden;}
  body{width:1200px;height:1200px;}
  .canvas{
    width:1200px;height:1200px;box-sizing:border-box;
    border:1px solid #b9bfc4;
    background:radial-gradient(circle at 50% 50%, var(--bg-center) 30%, var(--bg-edge) 100%);
  }
  .module-stack{display:block;width:1200px;height:1200px;}
  .brick-frame{fill:var(--frame);stroke:var(--frame);stroke-width:12;stroke-linejoin:miter;filter:drop-shadow(0 2px 3px rgba(0,0,0,.18));}
  .module-code{font-family:"Open Sans",sans-serif;font-weight:700;font-size:34px;fill:var(--label);}
  .module-name{font-family:"Open Sans",sans-serif;font-weight:600;font-size:15px;fill:var(--label);}
  .icon{fill:none;stroke:var(--label);stroke-width:5;stroke-linecap:round;stroke-linejoin:round;}
  .icon-fill{fill:var(--label);stroke:none;}
</style>
</head>
<body>
<div class="canvas">
<svg class="module-stack" viewBox="0 0 1181 1181" xmlns="http://www.w3.org/2000/svg" aria-label="Modulare Struktur des MES MORVIK 7 MAX">
  <defs>
    <path id="brick" d="M0,14 H30 V0 H58 V14 H107 V0 H135 V14 H185 V0 H213 V14 H242 V148 H0 Z"/>
    <path id="brick-base" d="M0,14 H30 V0 H58 V14 H107 V0 H135 V14 H185 V0 H213 V14 H285 V0 H313 V14 H362 V0 H390 V14 H440 V0 H468 V14 H540 V0 H568 V14 H617 V0 H645 V14 H695 V0 H723 V14 H748 V147 H0 Z"/>
    <linearGradient id="g-alarm" x1="0" y1="0" x2="0" y2="1"><stop offset="0" stop-color="#8c6c9c"/><stop offset=".5" stop-color="#573378"/><stop offset="1" stop-color="#44265f"/></linearGradient>
    <linearGradient id="g-mde" x1="0" y1="0" x2="0" y2="1"><stop offset="0" stop-color="#f2a2c2"/><stop offset=".5" stop-color="#e6559a"/><stop offset="1" stop-color="#de3f80"/></linearGradient>
    <linearGradient id="g-bde" x1="0" y1="0" x2="0" y2="1"><stop offset="0" stop-color="#d890c2"/><stop offset=".5" stop-color="#bf4a9a"/><stop offset="1" stop-color="#ab3688"/></linearGradient>
    <linearGradient id="g-inst" x1="0" y1="0" x2="0" y2="1"><stop offset="0" stop-color="#9c7ca2"/><stop offset=".5" stop-color="#7a3c80"/><stop offset="1" stop-color="#672c6e"/></linearGradient>
    <linearGradient id="g-dok" x1="0" y1="0" x2="0" y2="1"><stop offset="0" stop-color="#acd2ee"/><stop offset=".5" stop-color="#6cb2e2"/><stop offset="1" stop-color="#58a6dc"/></linearGradient>
    <linearGradient id="g-tnt" x1="0" y1="0" x2="0" y2="1"><stop offset="0" stop-color="#7cb2de"/><stop offset=".5" stop-color="#2888cc"/><stop offset="1" stop-color="#187ac4"/></linearGradient>
    <linearGradient id="g-em" x1="0" y1="0" x2="0" y2="1"><stop offset="0" stop-color="#6c7ab2"/><stop offset=".5" stop-color="#23448e"/><stop offset="1" stop-color="#183682"/></linearGradient>
    <linearGradient id="g-plan" x1="0" y1="0" x2="0" y2="1"><stop offset="0" stop-color="#c6de8c"/><stop offset=".5" stop-color="#98c63c"/><stop offset="1" stop-color="#88bc2c"/></linearGradient>
    <linearGradient id="g-log" x1="0" y1="0" x2="0" y2="1"><stop offset="0" stop-color="#7ec282"/><stop offset=".5" stop-color="#23a040"/><stop offset="1" stop-color="#169436"/></linearGradient>
    <linearGradient id="g-vis" x1="0" y1="0" x2="0" y2="1"><stop offset="0" stop-color="#6c8c6c"/><stop offset=".5" stop-color="#14553a"/><stop offset="1" stop-color="#0a4628"/></linearGradient>
    <linearGradient id="g-pep" x1="0" y1="0" x2="0" y2="1"><stop offset="0" stop-color="#fac272"/><stop offset=".5" stop-color="#f6a818"/><stop offset="1" stop-color="#f29e00"/></linearGradient>
    <linearGradient id="g-mpze" x1="0" y1="0" x2="0" y2="1"><stop offset="0" stop-color="#f4aa72"/><stop offset=".5" stop-color="#ea7422"/><stop offset="1" stop-color="#e6620e"/></linearGradient>
    <linearGradient id="g-dnc" x1="0" y1="0" x2="0" y2="1"><stop offset="0" stop-color="#f08c72"/><stop offset=".5" stop-color="#e23224"/><stop offset="1" stop-color="#dc1c16"/></linearGradient>
    <linearGradient id="g-basis" x1="0" y1="0" x2="0" y2="1"><stop offset="0" stop-color="#cad6de"/><stop offset=".5" stop-color="#b0c2cc"/><stop offset="1" stop-color="#a0b6c2"/></linearGradient>
  </defs>

  <!-- ALARM -->
  <g class="module module-alarm" transform="translate(470,150)">
    <use href="#brick" class="brick-frame"/><use href="#brick" fill="url(#g-alarm)"/>
    <circle class="icon-fill" cx="58" cy="74" r="10"/>
    <path class="icon" d="M44,60 a20,20 0 0 0 0,28 M72,60 a20,20 0 0 1 0,28 M34,50 a34,34 0 0 0 0,48 M82,50 a34,34 0 0 1 0,48"/>
    <text class="module-code" x="118" y="72">ALARM</text>
    <text class="module-name" x="118" y="98">Alarmierung</text>
  </g>

  <!-- Row 1 -->
  <g class="module module-mde" transform="translate(215,292)">
    <use href="#brick" class="brick-frame"/><use href="#brick" fill="url(#g-mde)"/>
    <circle class="icon" cx="40" cy="88" r="12" stroke-dasharray="5 4" stroke-width="7"/>
    <circle class="icon" cx="40" cy="88" r="5" stroke-width="3"/>
    <circle class="icon" cx="34" cy="62" r="7" stroke-width="4"/>
    <circle class="icon" cx="60" cy="62" r="7" stroke-width="4"/>
    <path class="icon" d="M62,100 L88,70 L94,76 L68,106 L60,108 Z" stroke-width="4"/>
    <text class="module-code" x="113" y="66">MDE</text>
    <text class="module-name" x="113" y="93">Maschinen-</text>
    <text class="module-name" x="113" y="114">datenerfassung</text>
  </g>
  <g class="module module-bde" transform="translate(470,292)">
    <use href="#brick" class="brick-frame"/><use href="#brick" fill="url(#g-bde)"/>
    <path class="icon" d="M22,48 V108 H86" stroke-width="3"/>
    <rect class="icon-fill" x="32" y="70" width="8" height="34"/>
    <rect class="icon-fill" x="44" y="58" width="8" height="46"/>
    <rect class="icon-fill" x="56" y="80" width="8" height="24"/>
    <circle class="icon" cx="64" cy="70" r="12" stroke-width="4"/>
    <path class="icon" d="M73,79 L86,94" stroke-width="6"/>
    <text class="module-code" x="113" y="66">BDE</text>
    <text class="module-name" x="113" y="93">Betriebsdaten-</text>
    <text class="module-name" x="113" y="114">erfassung</text>
  </g>
  <g class="module module-inst" transform="translate(725,292)">
    <use href="#brick" class="brick-frame"/><use href="#brick" fill="url(#g-inst)"/>
    <path class="icon" d="M30,56 L78,104" stroke-width="8"/>
    <path class="icon" d="M82,54 L34,102" stroke-width="8"/>
    <circle class="icon" cx="30" cy="56" r="8" stroke-width="5"/>
    <path class="icon-fill" d="M78,48 L92,52 L86,66 L76,60 Z"/>
    <text class="module-code" x="113" y="80">INST</text>
    <text class="module-name" x="113" y="106">Instandhaltung</text>
  </g>

  <!-- Row 2 -->
  <g class="module module-dok" transform="translate(215,440)">
    <use href="#brick" class="brick-frame"/><use href="#brick" fill="url(#g-dok)"/>
    <path class="icon" d="M28,46 H64 L78,60 V110 H28 Z" stroke-width="5"/>
    <path class="icon" d="M38,70 H68 M38,80 H68 M38,90 H68 M38,100 H60" stroke-width="4"/>
    <text class="module-code" x="113" y="66">DOK</text>
    <text class="module-name" x="113" y="93">Dokumenten-</text>
    <text class="module-name" x="113" y="114">management</text>
  </g>
  <g class="module module-tnt" transform="translate(470,440)">
    <use href="#brick" class="brick-frame"/><use href="#brick" fill="url(#g-tnt)"/>
    <path class="icon" d="M26,62 H44 C58,62 60,98 76,98 H84 M26,98 H44 C58,98 60,62 76,62 H84" stroke-width="7"/>
    <path class="icon-fill" d="M82,52 L96,62 L82,72 Z M82,88 L96,98 L82,108 Z"/>
    <text class="module-code" x="113" y="76">TNT</text>
    <text class="module-name" x="113" y="104">Traceability</text>
  </g>
  <g class="module module-em" transform="translate(725,440)">
    <use href="#brick" class="brick-frame"/><use href="#brick" fill="url(#g-em)"/>
    <rect class="icon" x="26" y="62" width="60" height="30" stroke-width="4"/>
    <rect class="icon-fill" x="88" y="70" width="5" height="14"/>
    <path class="icon-fill" d="M66,66 H82 V88 H60 Z"/>
    <text class="module-code" x="113" y="66">EM</text>
    <text class="module-name" x="113" y="93">Energie-</text>
    <text class="module-name" x="113" y="114">monitoring</text>
  </g>

  <!-- Row 3 -->
  <g class="module module-plan" transform="translate(215,588)">
    <use href="#brick" class="brick-frame"/><use href="#brick" fill="url(#g-plan)"/>
    <rect class="icon" x="26" y="56" width="58" height="50" rx="5" stroke-width="4"/>
    <path class="icon" d="M26,68 H84 M40,50 V60 M70,50 V60" stroke-width="4"/>
    <rect class="icon-fill" x="33" y="74" width="12" height="10"/><rect class="icon-fill" x="49" y="74" width="12" height="10"/><rect class="icon-fill" x="65" y="74" width="12" height="10"/>
    <rect class="icon-fill" x="33" y="88" width="12" height="10"/><rect class="icon-fill" x="49" y="88" width="12" height="10"/><rect class="icon-fill" x="65" y="88" width="12" height="10"/>
    <text class="module-code" x="113" y="64">PLAN</text>
    <text class="module-name" x="113" y="91">Feinplanung/</text>
    <text class="module-name" x="113" y="112">Leitstand</text>
  </g>
  <g class="module module-log" transform="translate(470,588)">
    <use href="#brick" class="brick-frame"/><use href="#brick" fill="url(#g-log)"/>
    <path class="icon-fill" d="M24,58 H66 L80,72 L92,78 V94 H24 Z"/>
    <circle cx="40" cy="96" r="8" fill="#1c9a3a" stroke="#fff" stroke-width="4"/>
    <circle cx="76" cy="96" r="8" fill="#1c9a3a" stroke="#fff" stroke-width="4"/>
    <text class="module-code" x="113" y="76">LOG</text>
    <text class="module-name" x="113" y="104">Logistik</text>
  </g>
  <g class="module module-vis" transform="translate(725,588)">
    <use href="#brick" class="brick-frame"/><use href="#brick" fill="url(#g-vis)"/>
    <path class="icon" d="M24,80 C40,58 74,58 90,80 C74,102 40,102 24,80 Z" stroke-width="5"/>
    <circle class="icon" cx="57" cy="80" r="11" stroke-width="5"/>
    <circle class="icon-fill" cx="57" cy="80" r="4"/>
    <text class="module-code" x="113" y="76">VIS</text>
    <text class="module-name" x="113" y="104">Visualisierung</text>
  </g>

  <!-- Row 4 -->
  <g class="module module-pep" transform="translate(215,738)">
    <use href="#brick" class="brick-frame"/><use href="#brick" fill="url(#g-pep)"/>
    <circle class="icon-fill" cx="34" cy="62" r="6"/><circle class="icon-fill" cx="80" cy="62" r="6"/><circle class="icon-fill" cx="57" cy="70" r="7"/>
    <path class="icon-fill" d="M26,72 H42 V98 H38 V110 H30 V98 H26 Z M72,72 H88 V98 H84 V110 H76 V98 H72 Z M47,80 H67 V106 H62 V118 H52 V106 H47 Z"/>
    <text class="module-code" x="113" y="66">PEP</text>
    <text class="module-name" x="113" y="93">Personal-</text>
    <text class="module-name" x="113" y="114">einsatzplanung</text>
  </g>
  <g class="module module-mpze" transform="translate(470,738)">
    <use href="#brick" class="brick-frame"/><use href="#brick" fill="url(#g-mpze)"/>
    <circle class="icon" cx="57" cy="80" r="30" stroke-width="5"/>
    <path class="icon" d="M57,80 L57,62 M57,80 L72,86" stroke-width="4"/>
    <text class="module-code" x="113" y="66">MPZE</text>
    <text class="module-name" x="113" y="93">Personalzeit-</text>
    <text class="module-name" x="113" y="114">erfassung</text>
  </g>
  <g class="module module-dnc" transform="translate(725,738)">
    <use href="#brick" class="brick-frame"/><use href="#brick" fill="url(#g-dnc)"/>
    <rect class="icon-fill" x="48" y="52" width="18" height="16"/>
    <path class="icon" d="M57,68 V78 M30,88 V78 H84 V88 M57,78 V88" stroke-width="4" stroke-linecap="butt"/>
    <rect class="icon-fill" x="20" y="88" width="18" height="18"/><rect class="icon-fill" x="48" y="88" width="18" height="18"/><rect class="icon-fill" x="76" y="88" width="18" height="18"/>
    <text class="module-code" x="113" y="66">DNC</text>
    <text class="module-name" x="113" y="93">Rezepturen/</text>
    <text class="module-name" x="113" y="114">DNC</text>
  </g>

  <!-- BASIS -->
  <g class="module module-basis" transform="translate(215,888)">
    <use href="#brick-base" class="brick-frame"/><use href="#brick-base" fill="url(#g-basis)"/>
    <path class="icon-fill" d="M313,112 C300,92 290,80 290,66 A23,23 0 0 1 336,66 C336,80 326,92 313,112 Z"/>
    <circle cx="313" cy="65" r="8" fill="#b8c8d2"/>
    <text class="module-code" x="369" y="76">BASIS</text>
    <text class="module-name" x="369" y="104">Basismodul</text>
  </g>
</svg>
</div>
</body>
</html>
```